Visitenkarten-Design für App Start Up
Zielgruppe
Wir sind ein Start-Up und haben unsere Murento App gerelauncht.
Wir haben zwei Zielgruppen für unsere App. Zum einen lokale Gewerbetreibende, welche in Echtzeit Angebote (Coupons) erstellen können und zum anderen private User, welche diese innerhalb eines vorgegebenen Zeitraumes reservieren und einlösen können.
Hierfür müssen wir auch unsere Visitenkarten auf unser neues Design anpassen.
Aufgabenstellung
Visitenkarten sollten beidseitig bedruckt sein und auf der Vorderseite sollte unser Murento Logo und/oder der App Name Murento versehen sein. Auf der Rückseite benötigen wir die Infos: Name, Position, Firma inkl. Anschrift, E-Mail sowie die Telefonnummer.
Ansonsten freuen wir uns auf weitere kreative Ansätze.

```html
<!DOCTYPE html>
<html lang="de">
<head>
<meta charset="utf-8">
<title>Murento – Visitenkarte</title>
<link rel="stylesheet" href="https://fonts.googleapis.com/css2?family=Montserrat:wght@500;600&family=Fira+Sans:wght@400;600&display=swap">
<style>
  :root {
    --page: #ebebeb;
    --paper: #ffffff;
    --ink: #353a3f;
    --ink-soft: #4a4f55;
    --blue: #1e8fcc;
    --pink: #c2408f;
    --muted: #c9ccd0;
    --brand-font: "Montserrat", sans-serif;
    --text-font: "Fira Sans", sans-serif;
  }
  html, body {
    margin: 0;
    width: 1200px;
    height: 800px;
    overflow: hidden;
    background: var(--page);
  }
  .canvas {
    position: relative;
    width: 1200px;
    height: 800px;
  }
  .card {
    position: absolute;
    width: 560px;
    height: 320px;
    background: var(--paper);
    box-shadow: 0 6px 18px rgba(0,0,0,0.12);
    overflow: hidden;
  }

  /* Front side */
  .card--front { left: 90px; top: 70px; }
  .front-brand {
    position: absolute;
    left: 0; right: 0; top: 92px;
    display: flex;
    justify-content: center;
    align-items: center;
    gap: 14px;
  }
  .brand-square {
    width: 22px; height: 22px;
    background: var(--blue);
  }
  .brand-name {
    font-family: var(--brand-font);
    font-weight: 600;
    letter-spacing: 6px;
    color: var(--ink);
    font-size: 40px;
    line-height: 1;
  }
  .front-rule {
    position: absolute;
    left: 0; right: 0; top: 238px;
    height: 3px;
    background: var(--blue);
  }
  .front-tab {
    position: absolute;
    left: 140px; top: 216px;
    width: 280px; height: 48px;
    background: var(--blue);
    clip-path: polygon(18px 0, calc(100% - 18px) 0, 100% 14px, 100% calc(100% - 14px), calc(100% - 18px) 100%, 18px 100%, 0 calc(100% - 14px), 0 14px);
    display: flex; align-items: center; justify-content: center;
    font-family: var(--text-font);
    color: var(--paper);
    font-size: 22px;
    letter-spacing: 0.5px;
  }

  /* Back side */
  .card--back { left: 550px; top: 410px; }
  .back-dark {
    position: absolute;
    left: 0; top: 0; bottom: 0;
    width: 310px;
    background: var(--ink);
  }
  .back-brand {
    position: absolute;
    left: 0; width: 290px; top: 128px;
    text-align: center;
  }
  .back-brand .brand-row {
    display: flex; justify-content: center; align-items: center; gap: 12px;
  }
  .back-brand .brand-square { background: var(--pink); width: 18px; height: 18px; }
  .back-brand .brand-name { color: var(--paper); font-size: 34px; letter-spacing: 5px; }
  .back-brand .brand-web {
    margin-top: 14px;
    font-family: var(--text-font);
    color: var(--muted);
    font-size: 18px;
    letter-spacing: 0.5px;
  }
  .icon-strip {
    position: absolute;
    left: 292px; top: 58px;
    width: 52px; height: 236px;
    background: var(--blue);
    clip-path: polygon(0 0, calc(100% - 16px) 0, 100% 16px, 100% calc(100% - 16px), calc(100% - 16px) 100%, 0 100%);
  }
  .icon-strip svg {
    position: absolute;
    left: 13px;
    width: 24px; height: 24px;
    fill: none;
    stroke: var(--paper);
    stroke-width: 1.6;
    stroke-linecap: round;
    stroke-linejoin: round;
  }
  .contact {
    position: absolute;
    left: 372px; top: 50px; right: 20px;
    font-family: var(--text-font);
    color: var(--ink);
  }
  .contact-name {
    font-size: 26px;
    line-height: 1;
    white-space: nowrap;
  }
  .contact-name strong { font-weight: 600; }
  .contact-rule {
    height: 1px;
    background: var(--ink);
    margin-top: 6px;
    width: 150px;
  }
  .contact-role {
    font-size: 10px;
    font-weight: 600;
    letter-spacing: 0.8px;
    color: var(--blue);
    margin-top: 4px;
  }
  .contact-list {
    list-style: none;
    margin: 0; padding: 0;
    position: absolute;
    left: 0; top: 92px;
    font-size: 15px;
    color: var(--ink-soft);
  }
  .contact-list li { height: 48px; }
</style>
</head>
<body>
<main class="canvas">

  <section class="card card--front" aria-label="Vorderseite">
    <div class="front-brand">
      <span class="brand-square"></span>
      <span class="brand-name">MURENTO</span>
    </div>
    <div class="front-rule"></div>
    <div class="front-tab">www.murento.de</div>
  </section>

  <section class="card card--back" aria-label="Rückseite">
    <div class="back-dark"></div>
    <div class="back-brand">
      <div class="brand-row">
        <span class="brand-square"></span>
        <span class="brand-name">MURENTO</span>
      </div>
      <div class="brand-web">www.murento.de</div>
    </div>

    <div class="icon-strip">
      <svg viewBox="0 0 24 24" style="top:24px" aria-hidden="true">
        <circle cx="12" cy="8" r="4"/><path d="M4 21c1-4.5 4.5-7 8-7s7 2.5 8 7"/>
      </svg>
      <svg viewBox="0 0 24 24" style="top:84px" aria-hidden="true">
        <path d="M12 22s-7-7-7-12a7 7 0 0 1 14 0c0 5-7 12-7 12z"/><circle cx="12" cy="10" r="2.5"/>
      </svg>
      <svg viewBox="0 0 24 24" style="top:132px" aria-hidden="true">
        <path d="M5 3h4l2 5-2.5 1.5a11 11 0 0 0 6 6L16 13l5 2v4a2 2 0 0 1-2 2A17 17 0 0 1 3 5a2 2 0 0 1 2-2z"/>
      </svg>
      <svg viewBox="0 0 24 24" style="top:180px" aria-hidden="true">
        <rect x="3" y="5" width="18" height="14" rx="1.5"/><path d="M3 6l9 7 9-7"/>
      </svg>
    </div>

    <div class="contact">
      <div class="contact-name">Name <strong>Surname</strong></div>
      <div class="contact-rule"></div>
      <div class="contact-role">SALES MANAGER</div>
      <ul class="contact-list">
        <li>Sample Street 22</li>
        <li>+41 23 456 789</li>
        <li>hallo@murento.de</li>
      </ul>
    </div>
  </section>

</main>
</body>
</html>
```